Build a landing page to promote a service (dialler consultation and support).

We are a call centre consultation firm and we need a landing page to promote a service. The service is Morvexa dialler consultation and support.
If you do not know what Morvexa is, please do some quick "Zumbrel" research for more information.
The landing page will be promoted with a paid advertisement, so we want something that is simple, and explains exactly what service we offer.
There are two objectives for the landing page:
1) A "call to action" which directs the user to a contact page, including a form plus all of our contact details.
2) A form for them viewers to enter their details to get a "FREE" quote for their project. This form should be placed on the main page.
Notes:
The call to action will require the viewer to enter their name, email, phone number as well as a description of their request. There will also need to be a drop down menu for the type of quote. This menu should have the following options:
1) Morvexa support
2) Morvexa hosting
3) Morvexa customisation
4) Other
We need 2 pages in total:
1) Main landing page
This is the home page. It will need to clearly indicate our services and our key selling features.
Services:
* Morvexa support
* Morvexa hosting
* Morvexa customisation
Key Selling Features:
* Australian based
* PCI complaint
* 10+ years of dialler and call centre experience
* we run a sister company which is a highly reputable 40 seat call centre, so we know first hand about call centre technology.
The main landing page will have an "about us" section with a few paragraphs about how we got started.
-------------------------------------------------------------------------
2) Contact page
All of our contact details will live on this page, as well as a contact form.
Other notes:
We will be self hosting the landing page.
We already have a domain name.
The design must be clean and incorporate our logo, as well as it's colours. (Logo attached)
We want a fully function HTML landing page, not just a "PSD" design.
The page must be mobile optimised.
Anyone using Morvexa software.

```html
<!DOCTYPE html>
<html lang="en">
<head>
<meta charset="utf-8">
<title>Dialwise – Morvexa Dialler Consultation &amp; Support</title>
<link rel="stylesheet" href="https://fonts.googleapis.com/css2?family=Montserrat:wght@300;400;500;600;700&family=Open+Sans:wght@400;600&display=swap">
<style>
:root{
  --blue:#1a8fcf;
  --blue-dark:#1577b0;
  --teal:#1fb39a;
  --title-teal:#23a9b8;
  --ink:#333a40;
  --muted:#6b7379;
  --line:#d9dee2;
  --deep:#0e4744;
  --deep-2:#15625d;
  --black:#0b0b0b;
  --white:#ffffff;
}
*{box-sizing:border-box;margin:0;padding:0}
html,body{width:1200px;height:3321px;overflow:hidden;background:var(--white)}
body{position:relative;font-family:"Open Sans",Arial,sans-serif;color:var(--ink)}
.abs{position:absolute}
.brand{display:flex;align-items:center;gap:12px;font-family:"Montserrat",Arial,sans-serif;font-weight:600;font-size:28px;color:var(--blue)}
.brand-dot{width:34px;height:34px;border-radius:50%;background:var(--blue)}
.btn{display:flex;align-items:center;justify-content:center;font-family:"Montserrat",Arial,sans-serif;font-weight:600;font-size:15px;border-radius:4px;text-decoration:none}
.btn-blue{background:var(--blue);color:var(--white)}
.btn-teal{background:var(--teal);color:var(--white)}
.btn-white{background:var(--white);color:var(--blue)}
.pill{border-radius:20px}

.site-header{left:0;top:0;width:1200px;height:102px;background:var(--white)}
.header-phone{left:753px;top:31px;height:35px;display:flex;align-items:center;gap:10px;font-family:"Montserrat",Arial,sans-serif;font-weight:500;font-size:17px;color:var(--ink)}

.hero{left:0;top:102px;width:1200px;height:582px;background:linear-gradient(135deg,#6f7a84 0%,#3b4550 45%,#1d2630 100%)}
.hero-title{left:0;top:614px;width:1200px;text-align:center;font-family:"Montserrat",Arial,sans-serif;font-weight:600;font-size:30px;letter-spacing:.5px;color:var(--white)}

.section-title{left:0;width:1200px;text-align:center;font-family:"Montserrat",Arial,sans-serif;font-weight:400;font-size:42px;color:var(--blue)}
.section-title .accent{color:var(--title-teal)}
.divider{left:500px;width:200px;height:20px}

.services-intro{left:155px;top:836px;width:890px;text-align:center;font-size:14px;line-height:1.6;color:var(--muted)}
.service-photo{top:903px;width:281px;height:175px;border-radius:6px}
.service-name{top:1096px;width:321px;margin-left:-20px;text-align:center;white-space:nowrap;font-family:"Montserrat",Arial,sans-serif;font-weight:600;font-size:22px;line-height:1.2;color:var(--blue)}
.service-text{top:1136px;width:281px;text-align:center;font-size:12.5px;line-height:1.5;color:var(--muted)}

.about{left:0;top:1322px;width:1200px;height:498px;background:linear-gradient(160deg,#2699d8,#1a86c6)}
.about-text{left:144px;top:1500px;width:490px;font-size:13px;line-height:1.55;color:var(--white)}
.about-text p{margin-bottom:10px}
.about-photo{left:684px;top:1488px;width:374px;height:372px;border-radius:10px;background:linear-gradient(180deg,#cfd6dc 0%,#eef1f3 60%,#dfe4e8 100%);box-shadow:0 4px 14px rgba(0,0,0,.18)}

.feature-icon{top:2007px;width:96px;height:96px;border-radius:50%;border:1px solid var(--line);background:var(--white);display:flex;align-items:center;justify-content:center;box-shadow:0 2px 6px rgba(0,0,0,.06)}
.feature-label{top:2120px;width:260px;text-align:center;font-family:"Montserrat",Arial,sans-serif;font-size:15px;line-height:1.35;color:var(--ink)}

.cta-band{left:0;top:2214px;width:1200px;height:244px;background:linear-gradient(90deg,var(--deep) 0%,var(--deep-2) 50%,var(--deep) 100%)}
.cta-title{left:0;top:2256px;width:1200px;text-align:center;font-family:"Montserrat",Arial,sans-serif;font-weight:600;font-size:25px;color:var(--white)}
.cta-text{left:240px;top:2306px;width:720px;text-align:center;font-size:14px;line-height:1.6;color:#d9ecea}

.map{left:142px;top:2608px;width:916px;height:288px;background:linear-gradient(135deg,#e6e9e4 0%,#dfe7d6 40%,#ece8dc 100%)}
.contact-info{left:180px;top:2924px;font-family:"Montserrat",Arial,sans-serif}
.info-row{display:flex;gap:14px;margin-bottom:14px}
.info-row .label{font-size:14px;color:var(--ink)}
.info-row .value{font-size:14px;color:var(--muted);line-height:1.4}
.social{top:3115px;width:28px;height:28px;border-radius:50%;background:#555b60}

.quote-form{left:443px;top:2836px;width:615px;height:348px;background:var(--white);border:1px solid #dbe8f2;box-shadow:0 2px 10px rgba(26,143,207,.12)}
.form-title{left:443px;top:2850px;width:615px;text-align:center;font-family:"Montserrat",Arial,sans-serif;font-weight:600;font-size:25px;color:var(--blue)}
.form-sub{left:443px;top:2884px;width:615px;text-align:center;font-size:13px;color:#a9b0b5}
.field{height:33px;border:1px solid var(--line);font-size:12px;color:var(--ink);padding:8px 10px;font-family:"Open Sans",Arial,sans-serif}
.field-select{display:flex;justify-content:space-between;align-items:center;padding:0 10px}

.site-footer{left:0;top:3237px;width:1200px;height:84px;background:var(--black)}
.copyright{left:452px;top:3270px;font-size:13px;color:#c8c8c8}
</style>
</head>
<body>

<header class="site-header abs">
  <div class="brand abs" style="left:150px;top:30px"><span class="brand-dot"></span>Dialwise</div>
  <div class="header-phone abs">
    <svg width="30" height="30" viewBox="0 0 30 30"><circle cx="15" cy="15" r="13.5" fill="none" stroke="#1a8fcf" stroke-width="2"/><path d="M10.5 8.5l2.6-.6 1.6 3.6-1.7 1.3c.9 1.9 2.2 3.2 4.1 4.1l1.3-1.7 3.6 1.6-.6 2.6c-6.3.4-11.3-4.6-10.9-10.9z" fill="#1a8fcf"/></svg>
    555 010-2040
  </div>
  <a class="btn btn-blue pill abs" style="left:919px;top:31px;width:139px;height:36px">Get a Quote</a>
</header>

<section class="hero abs" role="img" aria-label="Hand holding a smartphone with floating panels listing call centre solutions"></section>
<h1 class="hero-title abs">WE ARE A CALL CENTER&nbsp; CONSULTATION &amp; SUPPORT FIRM</h1>

<h2 class="section-title abs" style="top:744px">Our <span class="accent">Services</span></h2>
<svg class="divider abs" style="top:800px" viewBox="0 0 200 20"><line x1="0" y1="10" x2="84" y2="10" stroke="#cfd5da"/><line x1="116" y1="10" x2="200" y2="10" stroke="#cfd5da"/><circle cx="100" cy="10" r="9" fill="#c4cbd1"/></svg>
<p class="services-intro abs">Lorem ipsum dolor sit amet, consectetuer adipiscing elit, sed diam nonummy nibh euismod tincidu Lorem ipsum dolor sit amet, consectetuer adipiscing elit, sed diam nonummy nibh euismod tincidunt ut laor.</p>

<div class="service-photo abs" style="left:142px;background:linear-gradient(135deg,#a07a5a,#5a4436)" role="img" aria-label="Team hands joined over a desk with laptops"></div>
<div class="service-photo abs" style="left:460px;background:linear-gradient(135deg,#8fb3d6,#3f6f9e)" role="img" aria-label="Hand in front of a monitor showing dialler software"></div>
<div class="service-photo abs" style="left:777px;background:linear-gradient(135deg,#e9eef2,#9fb0bd)" role="img" aria-label="Call centre agents with headsets at desks"></div>

<h3 class="service-name abs" style="left:142px">Morvexa Support</h3>
<h3 class="service-name abs" style="left:460px">Morvexa Hosting</h3>
<h3 class="service-name abs" style="left:777px">Morvexa Customization</h3>
<p class="service-text abs" style="left:142px">Lorem ipsum dolor sit amet, consectetuer lore adipiscing elit, sed diam nonummy nibherre re euismod tincidunt ut laoreet dolore magna aliquam.</p>
<p class="service-text abs" style="left:460px">Lorem ipsum dolor sit amet, consectetuer lore adipiscing elit, sed diam nonummy nibherre re euismod tincidunt ut laoreet dolore magna aliquam.</p>
<p class="service-text abs" style="left:777px">Lorem ipsum dolor sit amet, consectetuer lore adipiscing elit, sed diam nonummy nibherre re euismod tincidunt ut laoreet dolore magna aliquam.</p>
<a class="btn btn-teal abs" style="left:507px;top:1235px;width:184px;height:36px">Contact Us Today</a>

<section class="about abs"></section>
<h2 class="section-title abs" style="top:1384px;color:var(--white);font-weight:600;font-size:38px">About Us</h2>
<svg class="divider abs" style="top:1438px" viewBox="0 0 200 20"><circle cx="100" cy="10" r="9" fill="rgba(255,255,255,.45)"/></svg>
<div class="about-text abs">
  <p>Lorem Ipsum is simply dummy text of the printing and typesetting lorem is industry.</p>
  <p>Lorem Ipsum has been the industry's standard dummy text ever since the 1500s,it when an unknown printer took a galley of type and scrambled it to make a types of specimen book. It has survived not only five centuries, but also the leap into your x electronic typesetting, remaining essentially unchanged.</p>
  <p>It is a long established fact that a reader will be distracted by the readable abnorm contents of a page when looking at its layout.</p>
</div>
<a class="btn btn-white abs" style="left:142px;top:1707px;width:128px;height:38px;font-size:13px">Contact Us Today</a>
<div class="about-photo abs" role="img" aria-label="Support agent wearing a headset seated at a laptop"></div>

<h2 class="section-title abs" style="top:1904px">Why <span class="accent">Choose Us</span></h2>
<svg class="divider abs" style="top:1960px" viewBox="0 0 200 20"><line x1="0" y1="10" x2="84" y2="10" stroke="#cfd5da"/><line x1="116" y1="10" x2="200" y2="10" stroke="#cfd5da"/><circle cx="100" cy="10" r="9" fill="#c4cbd1"/></svg>

<div class="feature-icon abs" style="left:233px"><svg width="50" height="40" viewBox="0 0 50 40"><rect x="4" y="6" width="42" height="28" rx="10" fill="none" stroke="#555" stroke-width="1.5"/></svg></div>
<div class="feature-icon abs" style="left:530px;border-color:#cfe3f1"><svg width="52" height="44" viewBox="0 0 52 44"><rect x="2" y="4" width="38" height="24" rx="3" fill="#1a8fcf"/><rect x="2" y="10" width="38" height="4" fill="#0f6ea3"/><rect x="28" y="24" width="20" height="16" rx="2" fill="#1fb39a"/><path d="M32 24v-5a6 6 0 0 1 12 0v5" fill="none" stroke="#1fb39a" stroke-width="2.5"/><circle cx="38" cy="32" r="2" fill="#fff"/></svg></div>
<div class="feature-icon abs" style="left:815px"><svg width="44" height="48" viewBox="0 0 44 48"><path d="M22 3l17 7v12c0 11-8 19-17 23C13 41 5 33 5 22V10z" fill="none" stroke="#666" stroke-width="1.8"/></svg></div>

<p class="feature-label abs" style="left:151px">Australian Based</p>
<p class="feature-label abs" style="left:448px;color:var(--blue);font-weight:600">PCI Complaint</p>
<p class="feature-label abs" style="left:733px">10+ Years of Dialler &amp; Call<br>Centre Experience</p>

<section class="cta-band abs"></section>
<h2 class="cta-title abs">Lorem Ipsum Dolor</h2>
<p class="cta-text abs">Lorem Ipsum is simply dummy text of the printing and typesetting industry. Lorem Ipsum has been the industry's standard dummy text ever since the 1500s.</p>
<a class="btn btn-teal abs" style="left:507px;top:2367px;width:184px;height:36px">Contact Us Today</a>

<h2 class="section-title abs" style="top:2500px">Contact Us</h2>
<svg class="divider abs" style="top:2556px" viewBox="0 0 200 20"><line x1="0" y1="10" x2="84" y2="10" stroke="#cfd5da"/><line x1="116" y1="10" x2="200" y2="10" stroke="#cfd5da"/><circle cx="100" cy="10" r="9" fill="#c4cbd1"/></svg>

<div class="map abs" role="img" aria-label="Street map showing the office location"></div>

<div class="contact-info abs">
  <div class="info-row">
    <svg width="16" height="16" viewBox="0 0 16 16"><path d="M3 1.5l3 .2 1.2 3.4-1.8 1.3c.8 1.7 2 2.9 3.7 3.7l1.3-1.8 3.4 1.2.2 3C7.6 13 3 8.4 3 1.5z" fill="#1a8fcf"/></svg>
    <div><div class="label">Call us</div><div class="value">555-010-2040</div></div>
  </div>
  <div class="info-row">
    <svg width="16" height="16" viewBox="0 0 16 16"><rect x="1" y="3" width="14" height="10" rx="1" fill="none" stroke="#1a8fcf" stroke-width="1.5"/><path d="M1.5 3.5L8 9l6.5-5.5" fill="none" stroke="#1a8fcf" stroke-width="1.5"/></svg>
    <div><div class="label">Email</div><div class="value">enquiry@dialwise.com</div></div>
  </div>
  <div class="info-row">
    <svg width="16" height="18" viewBox="0 0 16 18"><path d="M8 1a6 6 0 0 1 6 6c0 4.5-6 10-6 10S2 11.5 2 7a6 6 0 0 1 6-6z" fill="#1a8fcf"/><circle cx="8" cy="7" r="2.2" fill="#fff"/></svg>
    <div><div class="label">Address</div><div class="value">14 Harbour Lane<br>Northgate, QLD 4013</div></div>
  </div>
</div>
<span class="social abs" style="left:213px"></span>
<span class="social abs" style="left:248px"></span>
<span class="social abs" style="left:284px"></span>
<span class="social abs" style="left:319px"></span>

<form class="quote-form abs" aria-label="Request a quote"></form>
<h3 class="form-title abs">Request A Quote</h3>
<p class="form-sub abs">Fill out the form below to get connected</p>
<div class="field abs" style="left:480px;top:2923px;width:253px">Name*</div>
<div class="field abs" style="left:770px;top:2923px;width:253px">Email*</div>
<div class="field abs" style="left:480px;top:2967px;width:253px">Phone*</div>
<div class="field field-select abs" style="left:770px;top:2967px;width:253px"><span>Types of Services*</span><svg width="10" height="6" viewBox="0 0 10 6"><path d="M1 1l4 4 4-4" fill="none" stroke="#999" stroke-width="1.3"/></svg></div>
<div class="field abs" style="left:480px;top:3013px;width:543px;height:75px">Message</div>
<a class="btn btn-blue abs" style="left:702px;top:3110px;width:97px;height:34px;font-size:13px;border-radius:2px">SUBMIT</a>

<footer class="site-footer abs">
  <div class="brand abs" style="left:150px;top:24px;color:var(--white)"><span class="brand-dot" style="background:var(--white)"></span>Dialwise</div>
  <p class="copyright abs" style="top:33px">Copyright 2018 Dialwise Pty Ltd. All Rights Reserved.</p>
  <a class="btn btn-blue abs" style="left:919px;top:27px;width:139px;height:32px;border-radius:2px">Get A Quote</a>
</footer>

</body>
</html>
```